HLT Crown Business Card Design 2020

Our Manor Steward is looking for a business card that is clean and straight to the point but still looks high-end and attractive. We are a team comprised of management and field professionals focused on the high-end residential marketplace. We serve homeowners and trade professionals directly based out of the Metrowest/Boston area. We provide client services as well as construction/renovation services.
We are aiming for a black and white feel (white background and black text) and a matte finish with rounded edges.

We want to emphasis our vision of "Properties - Projects - Partners".
Dana Fellmore is the president of HLT

Please include the following areas we service: Boston/Cape/Newport
Please make sure to include Dana's mobile (555) 302 4187 & office number (555) 640 2913, email dana@ourmanorsteward.example and website www.ourmanorsteward.example

Colors

Designer to choose only greyscale colors for use in the design.

Requirements
Must have
• Include "Properties - Projects - Partners" in design

Include "After Hours Emergency Support # 1800 555 0142" with icon

```html
<!DOCTYPE html>
<html lang="en">
<head>
<meta charset="utf-8">
<title>HLT Crown Business Card</title>
<link rel="stylesheet" href="https://fonts.googleapis.com/css2?family=Poppins:wght@400;500;600;700&display=swap">
<style>
  :root {
    --page: #d9d9d9;
    --card-light: #ffffff;
    --card-dark: #2b2b2b;
    --ink: #1c1c1c;
    --ink-soft: #3a3a3a;
    --paper-text: #f4f4f4;
    --paper-muted: #d0d0d0;
    --divider: #8a8a8a;
  }
  * { box-sizing: border-box; margin: 0; padding: 0; }
  html, body { width: 1200px; height: 800px; overflow: hidden; }
  body {
    background: var(--page);
    font-family: "Poppins", sans-serif;
    position: relative;
  }
  .card {
    position: absolute;
    top: 245px;
    width: 525px;
    height: 310px;
    border-radius: 22px;
    overflow: hidden;
  }
  /* Front */
  .card--front {
    left: 50px;
    background: var(--card-light);
    color: var(--ink);
    display: flex;
    flex-direction: column;
    align-items: center;
    justify-content: center;
    gap: 26px;
  }
  .brand {
    display: flex;
    align-items: center;
    gap: 12px;
  }
  .brand__mark {
    width: 22px;
    height: 22px;
    background: currentColor;
  }
  .brand__name {
    font-weight: 700;
    font-size: 30px;
    letter-spacing: 0.04em;
    text-transform: uppercase;
  }
  .tagline {
    font-size: 15px;
    font-weight: 400;
    letter-spacing: 0.28em;
    text-transform: uppercase;
    color: var(--ink-soft);
  }
  /* Back */
  .card--back {
    left: 625px;
    background: var(--card-dark);
    color: var(--paper-text);
  }
  .card--back .brand {
    position: absolute;
    left: 32px;
    top: 88px;
    width: 180px;
    flex-direction: column;
    align-items: flex-start;
    gap: 10px;
  }
  .card--back .brand__name { font-size: 22px; line-height: 1.15; }
  .card--back .brand__mark { width: 18px; height: 18px; }
  .divider {
    position: absolute;
    left: 228px;
    top: 36px;
    width: 1px;
    height: 160px;
    background: var(--divider);
  }
  .contact {
    position: absolute;
    left: 250px;
    top: 38px;
    right: 18px;
  }
  .contact__name {
    font-weight: 700;
    font-size: 17px;
    letter-spacing: 0.02em;
    text-transform: uppercase;
  }
  .contact__role {
    font-size: 12px;
    color: var(--paper-muted);
    margin-bottom: 14px;
  }
  .contact__list { list-style: none; }
  .contact__item {
    display: flex;
    align-items: center;
    gap: 8px;
    font-size: 11.5px;
    line-height: 1.75;
  }
  .contact__item svg, .emergency svg { width: 12px; height: 12px; flex: none; }
  .emergency {
    position: absolute;
    left: 18px;
    right: 18px;
    top: 214px;
    display: flex;
    align-items: center;
    justify-content: center;
    gap: 8px;
    font-size: 11.5px;
    font-weight: 500;
    color: var(--paper-text);
  }
  .areas {
    position: absolute;
    left: 0; right: 0; bottom: 26px;
    height: 34px;
    background: var(--card-light);
    color: var(--ink);
    display: flex;
    align-items: center;
    justify-content: center;
    font-size: 13.5px;
    font-weight: 500;
    letter-spacing: 0.03em;
  }
</style>
</head>
<body>
  <section class="card card--front" aria-label="Card front">
    <div class="brand">
      <span class="brand__mark" aria-hidden="true"></span>
      <span class="brand__name">Our Manor Steward</span>
    </div>
    <p class="tagline">Properties - Projects - Partners</p>
  </section>

  <section class="card card--back" aria-label="Card back">
    <div class="brand">
      <span class="brand__mark" aria-hidden="true"></span>
      <span class="brand__name">Our Manor Steward</span>
    </div>
    <span class="divider" aria-hidden="true"></span>
    <div class="contact">
      <p class="contact__name">Dana Fellmore</p>
      <p class="contact__role">President of HLT</p>
      <ul class="contact__list">
        <li class="contact__item">
          <svg viewBox="0 0 12 12" aria-hidden="true"><rect x="3" y="0.8" width="6" height="10.4" rx="1" fill="none" stroke="currentColor" stroke-width="1.2"/></svg>
          (555) 302 4187
        </li>
        <li class="contact__item">
          <svg viewBox="0 0 12 12" aria-hidden="true"><path d="M2.5 1.5l2 0 .8 2.3-1.2 1a6 6 0 0 0 3.1 3.1l1-1.2 2.3.8v2c0 .6-.5 1-1.1 1A9 9 0 0 1 1.5 2.6c0-.6.4-1.1 1-1.1z" fill="currentColor"/></svg>
          (555) 640 2913
        </li>
        <li class="contact__item">
          <svg viewBox="0 0 12 12" aria-hidden="true"><rect x="0.8" y="2.3" width="10.4" height="7.4" fill="currentColor"/><path d="M1 2.6l5 4 5-4" fill="none" stroke="var(--card-dark)" stroke-width="1"/></svg>
          dana@ourmanorsteward.example
        </li>
        <li class="contact__item">
          <svg viewBox="0 0 12 12" aria-hidden="true"><circle cx="6" cy="6" r="5.2" fill="currentColor"/><path d="M1 6h10M6 1c-2.2 2.8-2.2 7.2 0 10M6 1c2.2 2.8 2.2 7.2 0 10" fill="none" stroke="var(--card-dark)" stroke-width=".7"/></svg>
          www.ourmanorsteward.example
        </li>
      </ul>
    </div>
    <p class="emergency">
      <svg viewBox="0 0 12 12" aria-hidden="true"><path d="M6 0.8l5.4 10H0.6z" fill="currentColor"/><path d="M6 4.3v3.2M6 8.6v.9" stroke="var(--card-dark)" stroke-width="1.2"/></svg>
      After Hours Emergency Support # 1800 555 0142
    </p>
    <p class="areas">Boston | Metrowest | South Shore | Cape | Newport</p>
  </section>
</body>
</html>
```